BLENOX - Joining Study and Progress for Fair Opportunity

Brochure is needed for the European Project "BLENOX". We will distribute this flyer during conferences and events to our audiences (mainly academics, researchers, business individuals, policy makers and members of civil society groups) in order to provide the basic information about the project.
The main scope of the project is to support research organisations across Europe to design and implement gender equality plans in order to promote the women’s position of the filed of STEM research.

We are providing a video to explain the layout: https://www.vidstreamhub.example/watch?v=Xk4pR9tLm2Z.
We think size can range from A4-A3.

We are attaching files to provide with concrete information on our requirements:
- BLENOX Brochure Layout_SA.ppt: includes the content we would like to include in the flyer. There is also the URL to the project website
- blenox Logo.zip: the project logo
- Partners Logos.zip: the Logos that will be included
We would like to use colours that belong to the project logo colour range. Regarding the images that you may include in the flyer, we wouldn't like to propose any because we do not want to limitate your imagination. We have some at the website https://blenox-project.example/. They could be diverse (age, race, gender, etc.) relevant to women and men.

```html
<!DOCTYPE html>
<html lang="en">
<head>
<meta charset="utf-8">
<title>BLENOX brochure</title>
<link href="https://fonts.googleapis.com/css2?family=Quicksand:wght@400;500;600&family=Montserrat:wght@300;400;500&display=swap" rel="stylesheet">
<style>
:root{
  --stage:#b3b3b8;
  --navy:#16162e;
  --navy-mid:#242352;
  --indigo:#3a3f8f;
  --indigo-soft:#4b4fa6;
  --gold:#f3b814;
  --paper:#ffffff;
  --paper-grey:#e3e3e6;
  --ink:#1d1d2b;
}
*{margin:0;padding:0;box-sizing:border-box}
html,body{width:831px;height:1200px;overflow:hidden}
body{background:var(--stage);position:relative;font-family:"Montserrat",sans-serif;color:var(--ink)}
.spread{position:absolute;left:33px;width:759px;display:flex;box-shadow:0 3px 8px rgba(0,0,0,.25)}
.spread--outer{top:38px;height:543px}
.spread--inner{top:633px;height:534px}
.page{position:relative;height:100%;overflow:hidden}

/* back cover */
.back{width:379px;background:var(--paper)}
.brand{position:absolute;display:flex;flex-direction:column;align-items:center}
.brand__name{font-family:"Quicksand",sans-serif;font-weight:500;color:var(--indigo);letter-spacing:1px}
.brand__dot{border-radius:50%;background:var(--gold)}
.brand__tag{font-family:"Quicksand",sans-serif;color:var(--indigo)}
.back .brand{left:26px;top:408px}
.back .brand__dot{width:14px;height:14px;margin-bottom:6px}
.back .brand__name{font-size:17px}
.back .brand__tag{font-size:4.6px}
.info{position:absolute;left:126px;top:418px;width:223px;height:88px;border:1px solid var(--indigo);border-left:none;padding:5px 6px 0 0;font-family:"Quicksand",sans-serif}
.info::before{content:"";position:absolute;left:0;top:-1px;width:28px;height:3px;background:var(--paper)}
.quote{position:absolute;font-family:"Montserrat",sans-serif;font-weight:500;color:var(--indigo);font-size:22px;line-height:1}
.quote--open{left:124px;top:404px}
.quote--close{left:186px;top:495px;background:var(--paper);padding:0 4px}
.info__link{font-size:5.4px;color:var(--indigo);line-height:1.3}
.info__line{font-size:5.4px;color:var(--ink);line-height:1.4}
.info__line span{color:var(--indigo)}
.info__head{font-size:6.2px;color:var(--gold);margin-top:5px}
.info__body{font-size:3.4px;line-height:1.35;margin-top:3px;text-align:justify}
.funding{display:flex;align-items:center;gap:4px;margin-top:6px}
.eu-flag{width:15px;height:10px;background:#1f3d99;flex:none}
.funding p{font-size:3.3px;color:var(--gold);line-height:1.3}

/* front cover */
.front{width:380px;background:linear-gradient(180deg,#16183a 0%,#1b1c3c 30%,#141428 100%)}
.front .brand{left:0;right:0;top:36px}
.front .brand__dot{width:26px;height:26px;margin-bottom:14px}
.front .brand__name{font-size:27px;letter-spacing:2px;color:var(--indigo-soft)}
.front .brand__tag{font-size:7px;color:var(--indigo-soft)}
.hero{position:absolute;left:0;top:160px;width:380px;height:250px;background:radial-gradient(ellipse at 55% 45%,#d9b48f 0%,#8d6f6a 30%,#3a3350 62%,#16162e 100%)}
.cover-title{position:absolute;left:0;right:0;top:438px;text-align:center;font-family:"Quicksand",sans-serif;color:var(--gold);font-size:22px;font-weight:500;line-height:1.2}
.cover-sub{position:absolute;left:0;right:0;top:494px;text-align:center;font-family:"Quicksand",sans-serif;color:var(--gold);font-size:9.5px;letter-spacing:4px}

/* inside left */
.inside-left{width:378px;background:var(--paper-grey)}
.team-photo{position:absolute;left:8px;top:30px;width:347px;height:187px;background:linear-gradient(160deg,#6d665d 0%,#bdb5a8 45%,#7c756e 100%)}
.band{position:absolute;left:0;background:linear-gradient(90deg,var(--indigo) 0%,var(--navy-mid) 100%);color:#fff;font-family:"Montserrat",sans-serif;font-weight:400;letter-spacing:3px}
.band--consortium{top:236px;width:180px;height:30px;font-size:15px;padding:6px 0 0 21px}
.band--hubs{top:344px;width:212px;height:36px;font-size:11.5px;line-height:1.2;padding:3px 0 0 28px}
.copy{position:absolute;left:10px;width:356px;font-size:6.3px;letter-spacing:1.1px;line-height:1.4;text-align:justify}
.copy--consortium{top:280px}
.copy--hubs{top:394px}
.bullets{list-style:none;margin:6px 0 6px 17px}
.bullets li{display:flex;align-items:center;gap:4px}
.bullets li::before{content:"";width:4px;height:4px;border-radius:50%;background:var(--indigo)}
.footer-left{position:absolute;left:10px;bottom:8px;right:12px;display:flex;justify-content:space-between;align-items:center}
.footer-left .funding{margin:0}
.footer-left .funding p{color:var(--indigo);font-size:3.6px}
.site{font-family:"Quicksand",sans-serif;font-size:8.5px;color:var(--indigo);letter-spacing:.4px}

/* inside right */
.inside-right{width:381px;background:var(--paper);overflow:visible}
.impact{position:absolute;left:-12px;top:29px;width:385px;height:188px;background:linear-gradient(90deg,var(--indigo) 0%,var(--navy-mid) 100%);color:#fff;padding:10px 14px 0 16px}
.impact::after{content:"";position:absolute;left:0;bottom:-8px;border-top:8px solid #1e1e46;border-left:12px solid transparent}
.impact h2{font-weight:400;font-size:11.5px;letter-spacing:2.5px;margin-bottom:8px}
.impact p{font-size:6.2px;letter-spacing:1.2px;line-height:1.4;text-align:justify}
.goal{position:absolute;display:flex;align-items:center;gap:4px;font-size:4.1px;letter-spacing:1px;line-height:1.4}
.goal svg{flex:none}
.goal--a{left:19px;top:116px;width:176px}
.goal--b{left:205px;top:114px;width:170px}
.goal--c{left:87px;top:146px;width:200px}
.partners{position:absolute;left:14px;top:246px;width:357px;display:grid;grid-template-columns:repeat(4,1fr);row-gap:22px;align-items:center;justify-items:center}
.badge{background:#c9cade}
.badge--wide{width:70px;height:22px;border-radius:3px}
.badge--round{width:30px;height:30px;border-radius:50%}
.badge--tall{width:36px;height:46px;border-radius:4px}
.social{position:absolute;left:0;right:0;top:493px;text-align:center;font-family:"Quicksand",sans-serif;color:var(--indigo)}
.social__row{display:flex;justify-content:center;gap:20px;font-size:6px}
.social__row span{display:flex;align-items:center;gap:4px}
.social__row span::before{content:"";width:6px;height:6px;background:var(--indigo)}
.social p{font-size:5.6px;margin-top:3px}
</style>
</head>
<body>

<section class="spread spread--outer">
  <div class="page back">
    <div class="brand">
      <div class="brand__dot"></div>
      <div class="brand__name">BLENOX</div>
      <div class="brand__tag">Gender Equality in STEM Research</div>
    </div>
    <span class="quote quote--open">&ldquo;</span>
    <div class="info">
      <p class="info__link">www.blenox-project.example/</p>
      <p class="info__link">info@blenox-project.example</p>
      <p class="info__line">Communication Manager: Marten Holvik <span>(mholvik@trevalabs.example)</span></p>
      <p class="info__head">The Goal</p>
      <p class="info__body">BLENOX project supports 7 RPOs and 2 RFOs, that are in an initial stage, to develop Gender Equality Plans (GEPs) and engage the local Innovation Hubs to transfer the gained knowledge beyond academia. The project goal is to make research organizations more gender equal by increasing the number of female researchers in STEM, improving their careers prospects and integrating a gender dimension in research.</p>
      <div class="funding">
        <div class="eu-flag"></div>
        <p>This project has received funding from the Northfield Research Fund programme under Grant Agreement No 550217</p>
      </div>
    </div>
    <span class="quote quote--close">&rdquo;</span>
  </div>

  <div class="page front">
    <div class="brand">
      <div class="brand__dot"></div>
      <div class="brand__name">BLENOX</div>
      <div class="brand__tag">Gender Equality in STEM Research</div>
    </div>
    <div class="hero" role="img" aria-label="Photo of hands typing on a laptop in warm light"></div>
    <h1 class="cover-title">Joining Study<br>and Progress</h1>
    <p class="cover-sub">for Fair Opportunity</p>
  </div>
</section>

<section class="spread spread--inner">
  <div class="page inside-left">
    <div class="team-photo" role="img" aria-label="Photo of a diverse team meeting around a conference table"></div>
    <h2 class="band band--consortium">Consortium</h2>
    <p class="copy copy--consortium">BLENOX consists of 7 Research Performing Organisations (RPOs) and 7 Research Funding Organisations (RFOs) to develop a GEP covering a wide area around Europe, including 8 EU countries, Turkey and Georgia. The project also includes 2 SMEs undertaking project coordination (TrevaLabs) and the scientific management (Smart Lagoon) and a professional association (Young Scholars Circle) to expand the project results.</p>
    <h2 class="band band--hubs">BLENOX Research<br>&amp; Innovation Hubs</h2>
    <div class="copy copy--hubs">
      <p>The RPOs/RFOs of the project establish local Research &amp; Innovation Hubs with the following stakeholders:</p>
      <ul class="bullets">
        <li>Academia and Universities</li>
        <li>Industry and Business</li>
        <li>Government &amp; Public Sector</li>
        <li>Civil society</li>
      </ul>
      <p>The strategic synergies stimulate dialogues to identify gaps and challenges related to gender inequalities at the different levels of the education-research-transfer to market and innovation chain.</p>
    </div>
    <div class="footer-left">
      <div class="funding">
        <div class="eu-flag"></div>
        <p>This project has received funding from the Northfield Research Fund<br>programme under Grant Agreement No 550217</p>
      </div>
      <span class="site">www.blenox-project.example</span>
    </div>
  </div>

  <div class="page inside-right">
    <div class="impact">
      <h2>Impact</h2>
      <p>BLENOX vision is to enhance the gender balance in STEM fields and promote a greater engagement of female researchers with research and innovation, contributing to the ERA1 priorities on Gender Equality and stimulating a dialogue and collaboration between academia, public authorities, professionals and industry players in order to tackle gender inequalities across the research-transfer-to-market chain.</p>
      <div class="goal goal--a">
        <svg width="16" height="18" viewBox="0 0 16 18" fill="none" stroke="#fff" stroke-width="1"><circle cx="5" cy="3" r="2"/><path d="M5 6v11M2 8h6M8 6h6v5h-6"/></svg>
        <span>Remove barriers to the recruitment, retention and career progression of female researchers</span>
      </div>
      <div class="goal goal--b">
        <svg width="18" height="18" viewBox="0 0 18 18" fill="none" stroke="#fff" stroke-width="1"><circle cx="5" cy="4" r="2.5"/><circle cx="13" cy="4" r="2.5"/><path d="M1 11h16M3 11v6M15 11v6M9 11v6"/></svg>
        <span>Improve the gender balance in decision-making bodies</span>
      </div>
      <div class="goal goal--c">
        <svg width="17" height="18" viewBox="0 0 17 18" fill="none" stroke="#fff" stroke-width="1"><rect x="3" y="1" width="11" height="7"/><path d="M6 6V4M8.5 6V3M11 6V5"/><circle cx="3" cy="12" r="1.6"/><circle cx="8.5" cy="12" r="1.6"/><circle cx="14" cy="12" r="1.6"/><path d="M1 17c0-2 4-2 4 0M6.5 17c0-2 4-2 4 0M12 17c0-2 4-2 4 0"/></svg>
        <span>Integrate the gender dimension in research and innovation content, improving the quality and societal relevance of produced knowledge, technologies and innovations.</span>
      </div>
    </div>
    <div class="partners" aria-label="Partner organisations">
      <div class="badge badge--wide"></div>
      <div class="badge badge--wide"></div>
      <div class="badge badge--tall"></div>
      <div class="badge badge--wide"></div>
      <div class="badge badge--wide"></div>
      <div class="badge badge--round"></div>
      <div class="badge badge--wide"></div>
      <div class="badge badge--round"></div>
      <div class="badge badge--tall"></div>
      <div class="badge badge--wide"></div>
      <div class="badge badge--round" style="width:38px;height:38px"></div>
      <div class="badge badge--round" style="width:38px;height:38px"></div>
    </div>
    <div class="social">
      <div class="social__row"><span>@BlenoxEU</span><span>Blenox EU</span><span>Blenox EU</span></div>
      <p>Follow BLENOX on social media platforms for the latest updates on project actions</p>
    </div>
  </div>
</section>

</body>
</html>
```